Design a single page Shopify store web page

We are looking to have a page designed for a single page Shopify store with 2 products. We already have a basic structure that we like, though we are open to suggestions. We are looking for somebody to provide a design/color scheme that we can then implement using Shopify's templating system. We can handle the implementation(HTML / CSS / jS) as we already have 2 web developers on the team, but have not been able to find a design we liked.

The job would consist of providing a mockup (photoshop or otherwise) and any vector graphics you choose to create for the site (we can provide product photos and other images).

You can also look at http://brickwellgoods.com.au for some of our design direction we have used so far

Target Market(s)

Young Australian Males (18 - 49)

Industry/Entity Type

Store

Number of Pages Required

1 page

Font styles to use
Serif
Sans Serif

Requirements
Must have
• Single Page Design
• E-commerce Product Purchase
• Manly (whatever interpretation of that you have)

```html
<!DOCTYPE html>
<html lang="en">
<head>
<meta charset="utf-8">
<title>Brickwell – How It Works</title>
<link rel="stylesheet" href="https://fonts.googleapis.com/css2?family=Arimo&family=Nunito+Sans:wght@400;700&family=Open+Sans:ital,wght@1,700&display=swap">
<style>
  :root {
    --header-bg: #333333;
    --page-bg: #e4e4e4;
    --column-bg: #d9d9d9;
    --circle-bg: #ffffff;
    --nav-text: #ffffff;
    --title-text: #5b5b5b;
    --body-text: #777777;
    --accent: #2a86e8;
    --icon-stroke: #5a5a5a;
  }
  * { margin: 0; padding: 0; box-sizing: border-box; }
  html, body { width: 1200px; height: 697px; overflow: hidden; }
  body { background: var(--page-bg); font-family: "Arimo", Arial, sans-serif; position: relative; }

  .site-header { position: absolute; left: 0; top: 0; width: 1200px; height: 99px; background: var(--header-bg); }
  .brand { position: absolute; left: 110px; top: 31px; font-family: "Nunito Sans", sans-serif; font-weight: 700; font-size: 34px; letter-spacing: 1.5px; color: var(--nav-text); line-height: 40px; }
  .main-nav a { position: absolute; top: 45px; font-family: "Nunito Sans", sans-serif; font-size: 13px; color: var(--nav-text); text-decoration: none; line-height: 16px; transform: translateX(-50%); white-space: nowrap; }
  .signup-button { position: absolute; left: 887px; top: 32px; width: 171px; height: 44px; background: #fff; color: var(--accent); font-family: "Open Sans", sans-serif; font-style: italic; font-weight: 700; font-size: 22px; line-height: 44px; text-align: center; text-decoration: none; }

  .section-title { position: absolute; left: 0; top: 172px; width: 1183px; text-align: center; font-family: "Nunito Sans", sans-serif; font-weight: 400; font-size: 53px; color: var(--title-text); line-height: 66px; }

  .step-column { position: absolute; top: 385px; width: 233px; height: 312px; background: var(--column-bg); }
  .step-icon { position: absolute; top: 292px; width: 218px; height: 218px; border-radius: 50%; background: var(--circle-bg); display: flex; align-items: center; justify-content: center; }
  .step-icon svg { fill: none; stroke: var(--icon-stroke); stroke-width: 4; stroke-linejoin: round; stroke-linecap: round; }
  .step-title { position: absolute; top: 537px; width: 320px; text-align: center; color: var(--accent); font-size: 23px; line-height: 30px; font-weight: 400; }
  .step-text { position: absolute; width: 320px; text-align: center; color: var(--body-text); font-size: 13.5px; line-height: 20px; }
</style>
</head>
<body>
  <header class="site-header">
    <div class="brand">BRICKWELL</div>
    <nav class="main-nav">
      <a href="#" style="left:416px">How It Works</a>
      <a href="#" style="left:540px">Plans</a>
      <a href="#" style="left:664px">FAQ</a>
      <a href="#" style="left:789px">About Us</a>
    </nav>
    <a class="signup-button" href="#">Sign Up Now!</a>
  </header>

  <h1 class="section-title">How It works</h1>

  <div class="step-column" style="left:181px"></div>
  <div class="step-column" style="left:459px"></div>
  <div class="step-column" style="left:735px"></div>

  <div class="step-icon" style="left:189px">
    <svg width="110" height="120" viewBox="0 0 110 120">
      <path d="M10 10 L60 8 L72 110 L20 112 Z"/>
      <path d="M22 38 l5 6 l9 -12 M24 64 l5 6 l9 -12 M26 90 l5 6 l9 -12"/>
      <path d="M95 20 L104 26 L60 98 L54 104 L52 94 Z"/>
    </svg>
  </div>
  <div class="step-icon" style="left:466px">
    <svg width="130" height="110" viewBox="0 0 130 110">
      <rect x="8" y="8" width="84" height="72"/>
      <line x1="8" y1="24" x2="92" y2="24"/>
      <text x="50" y="21" text-anchor="middle" font-family="Arimo, sans-serif" font-size="12" font-weight="700" fill="#5a5a5a" stroke="none">June</text>
      <text x="50" y="66" text-anchor="middle" font-family="Arimo, sans-serif" font-size="38" font-weight="700" fill="#5a5a5a" stroke="none">12</text>
      <path d="M78 82 l16 18 l30 -42" stroke-width="6"/>
    </svg>
  </div>
  <div class="step-icon" style="left:743px">
    <svg width="140" height="96" viewBox="0 0 140 96">
      <path d="M4 28 L40 4 L136 14 L104 40 Z"/>
      <path d="M4 28 L4 78 L104 92 L104 40 M104 92 L136 66 L136 14"/>
      <path d="M22 16 L120 27 L120 79"/>
      <path d="M88 9 L54 34 L54 85"/>
      <path d="M64 24 L72 30 L66 44 L58 38 Z"/>
    </svg>
  </div>

  <h2 class="step-title" style="left:138px">Choose a Plan</h2>
  <p class="step-text" style="left:140px; top:584px">There will be pants for all budgets and styles</p>

  <h2 class="step-title" style="left:417px">Choose How Often</h2>
  <p class="step-text" style="left:417px; top:574px">Decide whether you would like to<br>recieve new packages every 3 or 6 months</p>

  <h2 class="step-title" style="left:695px">Get Your Pack</h2>
  <p class="step-text" style="left:692px; top:574px">we'll send out your first pack&nbsp; right away<br>and then again every 3 or 6 months</p>
</body>
</html>
```